Modern Informational OBGYN website

Looking for a modern Wordpress website for a general OBGYN practice in Florida with a specialty in High Risk Obstetrics. We had an old Joomla website that crashed and we lost most of the files. It was over 10 years old and needed a refresh anyway.

Our practice serves a multicultural patient population (white, black, Spanish and Indian) and we would like our website to reflect that diversity. Our company colors are sunshine yellow (#ECBF6D) often combined with black, white and steel blue (#7191BE) in the "life" part of our logo (attached) depending on the background. Our tagline is "We're specialist in You!" Overall the site should have a clean modern yet comfortable feel. One that portrays friendliness and competence. At least 6 pages (Home, Obstetrics, Gynecology, News, Patient Education and Resources). Rotating stock pictures or videos are fine for the headers of the pages if the design you're considering calls for it. Interesting and creative use of typography and icons are encouraged.

The home page should have a call to action to schedule an appointment as well as a link to our patient portal. Other than the home and news pages, the other pages should have a similar look and feel. The home page should have sections on "About Us", "Medical Staff" (with pictures and brief bio for 2 male doctors, 2 female midwives and 1 female nurse practitioner), "Services" and "Location". The news page will be a closed blog that will not allow comments or responses. Both the obstetrics and the gynecology pages will have an educational blurb on the respective topics followed by a list of our services for each topic. Would be nice on the obstetrics page to have information and graphics changes that occur during each trimester (but not necessary). The resource page will have sections on at least "Office Forms", Office Policies", "OB Guide" each with multiple downloadable PDF's. Also a section on "Insurance" with a list of all the major insurance plans that we take with links to their company websites. The address, link and map to our hospital and their website can also go on this page. The Patient Education Page can be broken into 3 sections Obstetrics, Gynecology which both will have definition of medical disorders followed by FAQ's and "Helpful Links" which would have links to other website for medical information.

That's all that I can think of right now. The above is to help guide you but I am flexible, if the website design dictates a better flow of information. Looking forward to seeing what you can come up with. Down the road, I will be looking to the winning designer to produce matching brochures, full, half and quarter page media ads to have on hand for the practices further needs.

Target Market(s)

Women looking medical services

Industry/Entity Type

Medical

Coding

Coded - Design and coding required

Number of Pages Required

5+ page

Font styles to use
Sans Serif
Script

Colors

Designer to choose colors to be used in the design.

Requirements
Must have
• None. See projects description for suggestions
Nice to have
• infographics like information on stages of pregnancy on the obstetrics page

```html
<!DOCTYPE html>
<html lang="en">
<head>
<meta charset="utf-8">
<title>Brightday OB/GYN Services</title>
<link rel="stylesheet" href="https://fonts.googleapis.com/css2?family=Montserrat:wght@400;600;700;800&family=Open+Sans:ital,wght@0,400;0,600;0,700;1,400&family=Courgette&display=swap">
<style>
:root{
  --sun:#f1b02d;
  --sun-deep:#e29d12;
  --ink:#111111;
  --charcoal:#333333;
  --paper:#ffffff;
  --mist:#f6f6f6;
  --text:#3b3b3b;
  --line:#2a2a2a;
  --steel:#7191be;
}
*{box-sizing:border-box;margin:0;padding:0}
html,body{width:1200px;height:4222px;overflow:hidden}
body{position:relative;background:var(--paper);font-family:"Open Sans",Arial,sans-serif;color:var(--text)}
.abs{position:absolute}
.brand{display:flex;align-items:center;gap:10px;font-family:"Montserrat",Arial,sans-serif;font-weight:800;color:var(--sun);letter-spacing:1px}
.brand-dot{border-radius:50%;background:var(--sun);flex:none}
.brand small{display:block}
/* header */
.site-header .brand{left:74px;top:30px;font-size:34px}
.brand-dot.lg{width:40px;height:40px}
.brand-sub{left:126px;top:72px;font-family:"Montserrat",Arial,sans-serif;font-size:10px;letter-spacing:4px;color:var(--ink);font-weight:600}
.call{left:790px;top:38px;width:180px;text-align:center;font-family:"Montserrat",Arial,sans-serif}
.call .label{color:var(--sun);font-weight:600;font-size:18px}
.call .num{color:var(--ink);font-weight:700;font-size:19px;display:flex;align-items:center;justify-content:center;gap:6px}
.follow{left:960px;top:32px;width:120px;text-align:center;font-family:"Montserrat",Arial,sans-serif;color:var(--sun);font-weight:600;font-size:17px}
.social-row{display:flex;gap:3px;justify-content:center;margin-top:6px}
.social-row span{width:22px;height:22px;background:var(--steel);display:block}
.nav{left:0;top:105px;width:1200px;height:34px;background:var(--ink)}
.nav ul{list-style:none;display:flex;position:absolute;left:72px;top:0;height:34px}
.nav li{color:#fff;font-family:"Open Sans",Arial,sans-serif;font-size:16px;line-height:34px;padding:0 28px;border-right:1px solid #555}
.nav li.current{background:var(--sun);color:var(--ink);padding:0 28px;width:103px;text-align:center}
.cta-schedule{left:926px;top:102px;width:197px;height:44px;background:var(--sun);color:#fff;font-family:"Montserrat",Arial,sans-serif;font-weight:700;font-size:13px;text-align:center;line-height:14px;padding-top:8px;border-radius:2px}
/* hero */
.hero{left:0;top:139px;width:1200px;height:671px;background:linear-gradient(110deg,#c9c5c2 0%,#e6dfda 35%,#d8c2b2 60%,#c9a691 80%,#b88f7a 100%)}
.hero-title{left:200px;top:550px;width:810px;height:70px;background:rgba(255,255,255,.55);font-family:"Montserrat",Arial,sans-serif;font-weight:800;font-size:58px;color:#111;text-align:center;line-height:70px;letter-spacing:-1px}
.btn-book{left:480px;top:636px;width:244px;height:43px;border-radius:22px;background:var(--sun);color:#111;font-family:"Montserrat",Arial,sans-serif;font-weight:700;font-size:16px;letter-spacing:2px;text-align:center;line-height:43px}
/* headings */
.sec-title{font-family:"Montserrat",Arial,sans-serif;font-weight:700;font-size:36px;color:#111;display:flex;align-items:center;gap:10px}
.sec-title .accent{color:var(--sun)}
.sec-title .mark{width:22px;height:22px;border-radius:50%;background:var(--sun)}
.sec-title.light{color:#fff}
.pill{display:flex;align-items:center;justify-content:space-between;background:var(--ink);color:var(--sun);border-radius:14px;font-family:"Montserrat",Arial,sans-serif;font-weight:700;font-size:9px;letter-spacing:1px;padding:0 3px 0 9px}
.pill i{width:16px;height:16px;border-radius:50%;background:var(--sun);display:block;position:relative}
.pill i::after{content:"";position:absolute;left:5px;top:5px;width:5px;height:5px;border-top:2px solid #111;border-right:2px solid #111;transform:rotate(45deg)}
.pill.sunny{background:var(--sun);color:#111}
.pill.sunny i{background:#111}
.pill.sunny i::after{border-color:var(--sun)}
/* about */
.about-title{left:139px;top:878px}
.about-copy{left:139px;top:965px;width:432px;font-size:13.2px;line-height:16.4px;text-align:justify;color:#333}
.about-more{left:139px;top:1164px;width:95px;height:22px}
.about-photo{left:628px;top:880px;width:434px;height:318px;border:6px solid #cfe0e8;background:linear-gradient(120deg,#e9eef0,#d7dde0 45%,#c9bfb6 75%,#8f8680)}
/* services */
.services{left:0;top:1262px;width:1200px;height:657px;background:var(--charcoal)}
.services-title{left:0;top:1305px;width:1200px;justify-content:center}
.services-lead{left:200px;top:1398px;width:800px;text-align:center;color:#fff;font-style:italic;font-size:13px;line-height:16px}
.card{top:1467px;width:266px;height:339px;background:var(--sun);border:4px solid var(--sun)}
.card .img{height:190px;border:2px solid #fff}
.card h3{font-family:"Open Sans",Arial,sans-serif;font-weight:700;font-size:21px;color:#111;margin:20px 0 8px 20px;letter-spacing:1px}
.card p{margin:0 20px;font-size:12.6px;line-height:15.5px;color:#222;text-align:justify}
.more-services{left:544px;top:1847px;width:112px;height:22px}
/* news */
.news{left:0;top:1939px;width:1200px;height:713px;background:var(--mist)}
.news-title{left:139px;top:1985px}
.news-item{left:139px;width:520px;height:95px}
.date{position:absolute;left:0;top:0;width:87px;height:95px;font-family:"Montserrat",Arial,sans-serif;font-weight:700;text-align:center}
.date .d{height:50px;background:var(--sun);color:#fff;font-size:30px;line-height:50px}
.date .m{height:45px;background:var(--ink);color:#fff;font-size:20px;line-height:45px}
.news-item h4{position:absolute;left:108px;top:0;font-family:"Open Sans",Arial,sans-serif;font-weight:600;font-size:20px;color:var(--sun)}
.news-item p{position:absolute;left:108px;top:34px;width:408px;font-size:13px;line-height:16px;color:#222}
.news-more{left:139px;top:2550px;width:121px;height:27px}
.news-photo{left:688px;top:1975px;width:410px;height:677px;background:radial-gradient(ellipse at 50% 55%,#e7c0a8 0%,#dcb098 35%,#eeeeee 70%,#f6f6f6 100%)}
/* appointment */
.appt{left:0;top:2652px;width:1200px;height:656px;background:linear-gradient(100deg,#3e3a39 0%,#524c48 40%,#6a625d 70%,#48423f 100%)}
.appt-rule{left:148px;top:2687px;width:58px;height:1px;background:#888}
.appt-box{left:152px;top:2803px;width:899px;height:382px;background:rgba(212,156,36,.86)}
.appt-title{left:152px;top:2845px;width:899px;text-align:center;font-family:"Courgette",cursive;font-size:34px;color:#111}
.appt-sub{left:152px;top:2890px;width:899px;text-align:center;font-family:"Open Sans",Arial,sans-serif;font-style:italic;font-weight:600;font-size:18px;color:#fff}
.field{height:29px;background:#fff;border:1px solid #ddd;font-style:italic;font-size:12.5px;color:#999;padding-left:16px;line-height:27px}
.required{left:242px;top:3126px;font-style:italic;font-size:12.5px;color:#fff}
.btn-submit{left:649px;top:3130px;width:111px;height:25px;background:#111;color:#fff;border-radius:3px;font-size:12px;font-weight:700;text-align:center;line-height:25px}
/* faq */
.faq-title{left:0;top:3370px;width:1200px;justify-content:center}
.faq-q{left:136px;width:926px;font-family:"Open Sans",Arial,sans-serif;font-weight:600;font-size:20px;color:var(--sun)}
.faq-toggle{position:absolute;right:12px;top:-4px;font-size:26px;color:#111;font-weight:700}
.faq-a{left:136px;top:3490px;width:630px;font-size:13px;line-height:15.5px;color:#222;text-align:justify}
.faq-line{left:136px;width:926px;height:2px;background:var(--line)}
/* footer */
.footer{left:0;top:3868px;width:1200px;height:300px;background:var(--ink)}
.foot-brand{left:139px;top:3935px;font-size:32px}
.foot-brand-sub{left:190px;top:3975px;font-family:"Montserrat",Arial,sans-serif;font-size:9px;letter-spacing:4px;color:#fff;font-weight:600}
.foot-follow{left:141px;top:4040px;font-family:"Montserrat",Arial,sans-serif;font-weight:700;font-size:16px;color:var(--sun)}
.foot-icons{left:141px;top:4065px;display:flex;gap:7px}
.foot-icons span{width:30px;height:30px;border:2px solid #fff;border-radius:50%;display:block}
.divider{width:2px;background:#fff;top:3922px;height:176px}
.foot-head{font-family:"Montserrat",Arial,sans-serif;font-weight:700;font-size:18px;color:var(--sun)}
.foot-head b{color:#fff}
.contact-line{left:400px;display:flex;align-items:flex-start;gap:12px;color:#fff;font-size:13px;line-height:16px}
.links{left:639px;top:3998px;list-style:none;color:#fff;font-size:13px;line-height:18.4px}
.links li::before{content:"";display:inline-block;border-left:6px solid var(--sun);border-top:4px solid transparent;border-bottom:4px solid transparent;margin-right:10px}
.news-text{left:798px;top:4002px;width:280px;color:#fff;font-size:13px;line-height:17px}
.news-input{left:798px;top:4048px;width:256px;height:33px;background:#fff;font-size:12px;color:#333;padding-left:12px;line-height:33px}
.news-submit{left:798px;top:4099px;width:105px;height:33px;background:var(--sun);color:#fff;font-family:"Montserrat",Arial,sans-serif;font-weight:700;font-size:15px;text-align:center;line-height:33px;letter-spacing:1px}
.copyright{left:0;top:4168px;width:1200px;height:54px;background:var(--sun);text-align:center;line-height:54px;font-size:12px;color:#333}
</style>
</head>
<body>

<header class="site-header">
  <div class="abs brand"><span class="brand-dot lg"></span>BRIGHTDAY</div>
  <div class="abs brand-sub">OB/GYN SERVICES</div>
  <div class="abs call">
    <div class="label">Call us</div>
    <div class="num"><svg width="12" height="20" viewBox="0 0 12 20"><rect x="1" y="1" width="10" height="18" rx="2" fill="none" stroke="#111" stroke-width="2"/><rect x="4" y="15" width="4" height="2" fill="#111"/></svg>(012) 555-0142</div>
  </div>
  <div class="abs follow">Follow Us
    <div class="social-row"><span></span><span></span><span></span><span></span></div>
  </div>
</header>

<nav class="abs nav">
  <ul>
    <li class="current">Home</li>
    <li>Obstetrics</li>
    <li>Gynecology</li>
    <li>News</li>
    <li>Patient Education</li>
    <li>Resources</li>
  </ul>
</nav>
<div class="abs cta-schedule">SCHEDULE YOUR<br>APPOINTMENT</div>

<section>
  <div class="abs hero" role="img" aria-label="Smiling expectant mother receiving an ultrasound scan"></div>
  <h1 class="abs hero-title">WE'RE SPECIALIST IN YOU!</h1>
  <div class="abs btn-book">BOOK APPOINTMENT</div>
</section>

<section>
  <h2 class="abs sec-title about-title"><span class="mark"></span><span><span class="accent">ABOUT</span> US</span></h2>
  <p class="abs about-copy">Verum tamen cum de rebus grandioribus dicas, ipsae res verba rapiunt; Hoc non est positum in nostra actione. Quod ea non occurrentia fingunt, vincunt Aristonem; Haec para/doca illi, nos admirabilia dicamus. Et quidem, inquit, vehementer errat; Quarum ambarum rerum cum medicinam pollicetur, luxuriae licentiam pollicetur. Laelius clamores sofow ille so lebat Edere compellans gumias ex ordine nostros.Verum tamen cum de rebus grandioribus dicas, ipsae res verba rapiunt; Hoc non est positum in nostra actione. Quod ea non occurrentia fingunt, vincunt Aristonem; Haec para/doca illi, nos admirabilia dicamus. Et quidem, inquit, vehementer errat; Quarum ambarum</p>
  <div class="abs pill about-more">LEARN MORE<i></i></div>
  <div class="abs about-photo" role="img" aria-label="Doctor consulting with an expectant patient in the office"></div>
</section>

<section>
  <div class="abs services"></div>
  <h2 class="abs sec-title light services-title"><span class="mark"></span><span><span class="accent">OUR</span> SERVICES</span></h2>
  <p class="abs services-lead">Philosophorum praeceptis instituta vita superabat. Et quod est munus, quod opus sapientiae Non modo carum sibi quemque verum etiam vehementer philosophorum praeceptis instituta vita superabat.</p>
  <article class="abs card" style="left:139px">
    <div class="img" role="img" aria-label="Expectant mother during an ultrasound" style="background:linear-gradient(120deg,#d9d6d3,#e8ddd6 50%,#c8a591)"></div>
    <h3>FORTUNAE</h3>
    <p>Eteres philosophorum praeceptis instituta vita superabat. Et quod est munus, quod opus sapientiaEt quod est munus.</p>
  </article>
  <article class="abs card" style="left:469px">
    <div class="img" role="img" aria-label="Pregnant woman speaking with a clinician" style="background:linear-gradient(120deg,#dedede,#a9a4a2 45%,#6b5248 70%,#e4e4e4)"></div>
    <h3>GRANDIORIBU</h3>
    <p>Philosophorum praeceptis instituta vita superabat.eteres quod est munus, quod opus sapientiaEt quod est munus.</p>
  </article>
  <article class="abs card" style="left:800px">
    <div class="img" role="img" aria-label="Clinician examining a pregnant patient" style="background:linear-gradient(120deg,#e6e6e6,#b9aeb0 40%,#e8e8ea 70%,#cfc8c4)"></div>
    <h3>RESPONDEAT</h3>
    <p>Munus eteres philosophorum praeceptis instituta vita superabat. Et quod est , quod opus sapientiaEt quod est munus.</p>
  </article>
  <div class="abs pill sunny more-services">MORE SERVICES<i></i></div>
</section>

<section>
  <div class="abs news"></div>
  <h2 class="abs sec-title news-title"><span class="mark"></span><span><span class="accent">LATEST</span> NEWS</span></h2>
  <article class="abs news-item" style="top:2095px">
    <div class="date"><div class="d">08</div><div class="m">MAY</div></div>
    <h4>Luxuriae licentiam polliceturLaelius</h4>
    <p>Itaque primos congressus copulationesque et consuetudinum instituendarum voluntates fieri propter Itaque primos congressus copulationesque et consuetudinum</p>
  </article>
  <article class="abs news-item" style="top:2249px">
    <div class="date"><div class="d">08</div><div class="m">MAY</div></div>
    <h4>Luxuriae licentiam polliceturLaelius</h4>
    <p>Itaque primos congressus copulationesque et consuetudinum instituendarum voluntates fieri propter Itaque primos congressus copulationesque et consuetudinum</p>
  </article>
  <article class="abs news-item" style="top:2403px">
    <div class="date"><div class="d">08</div><div class="m">MAY</div></div>
    <h4>Luxuriae licentiam polliceturLaelius</h4>
    <p>Itaque primos congressus copulationesque et consuetudinum instituendarum voluntates fieri propter Itaque primos congressus copulationesque et consuetudinum</p>
  </article>
  <div class="abs pill news-more">LEARN MORE<i></i></div>
  <div class="abs news-photo" role="img" aria-label="Pregnant woman holding her belly"></div>
</section>

<section>
  <div class="abs appt" role="img" aria-label="Softly lit photo of a mother at an ultrasound appointment"></div>
  <div class="abs appt-rule"></div>
  <div class="abs appt-box"></div>
  <h2 class="abs appt-title">Request an appointment</h2>
  <p class="abs appt-sub">Get your family off to a smiling start&nbsp; Form</p>
  <div class="abs field" style="left:234px;top:2944px;width:366px">Your Name</div>
  <div class="abs field" style="left:639px;top:2944px;width:366px">Select Service</div>
  <div class="abs field" style="left:234px;top:3008px;width:366px">Your Email</div>
  <div class="abs field" style="left:639px;top:3008px;width:182px">Select Date</div>
  <div class="abs field" style="left:829px;top:3008px;width:176px">Select Time</div>
  <div class="abs field" style="left:234px;top:3075px;width:366px">Your Phone numer</div>
  <div class="abs field" style="left:639px;top:3075px;width:366px">Your Message Here</div>
  <div class="abs required">* Required Field</div>
  <div class="abs btn-submit">Submit</div>
</section>

<section>
  <h2 class="abs sec-title faq-title"><span class="mark"></span><span>FAQ’S</span></h2>
  <div class="abs faq-q" style="top:3452px">Est enim effectrix multarum et magnarum voluptatum<span class="faq-toggle">&minus;</span></div>
  <p class="abs faq-a">Grandioribus dicas, ipsae res verba rapiunt; Hoc non est positum in nostra actione. Quod ea non occurrentia fingunt, vincunt Aristonem; Haec para/doca illi, nos admirabilia dicamus. Et quidem, inquit, vehementer errat; Quarum ambarum rerum .</p>
  <div class="abs faq-q" style="top:3575px">Est enim effectrix multarum et ?<span class="faq-toggle">+</span></div>
  <div class="abs faq-line" style="top:3609px"></div>
  <div class="abs faq-q" style="top:3662px">Est enim effectrix multarum et ?<span class="faq-toggle">+</span></div>
  <div class="abs faq-line" style="top:3698px"></div>
  <div class="abs faq-q" style="top:3750px">Est enim effectrix multarum et ?<span class="faq-toggle">+</span></div>
  <div class="abs faq-line" style="top:3790px"></div>
</section>

<footer>
  <div class="abs footer"></div>
  <div class="abs brand foot-brand"><span class="brand-dot lg"></span>BRIGHTDAY</div>
  <div class="abs foot-brand-sub">OB/GYN SERVICES</div>
  <div class="abs foot-follow">FOLLOW US</div>
  <div class="abs foot-icons"><span></span><span></span><span></span><span></span></div>
  <div class="abs divider" style="left:360px"></div>
  <div class="abs foot-head" style="left:400px;top:3922px">CONTACT <b>US</b></div>
  <div class="abs contact-line" style="top:3998px">
    <svg width="12" height="16" viewBox="0 0 12 16"><path d="M6 0C2.7 0 0 2.6 0 5.9 0 10 6 16 6 16s6-6 6-10.1C12 2.6 9.3 0 6 0z" fill="#f1b02d"/><circle cx="6" cy="6" r="2.2" fill="#111"/></svg>
    <span>1420 Harbor View Road<br>Tampa, Florida 33602</span></div>
  <div class="abs contact-line" style="top:4050px">
    <svg width="14" height="14" viewBox="0 0 14 14"><path d="M3 0l2.5 3.5-1.5 1.8c.8 1.8 2.2 3.2 4 4l1.8-1.5L14 10.5 12 14C5.5 13.5.5 8.5 0 2z" fill="#f1b02d"/></svg>
    <span>813 555 0198</span></div>
  <div class="abs contact-line" style="top:4082px">
    <svg width="14" height="11" viewBox="0 0 14 11"><rect width="14" height="11" fill="#f1b02d"/><path d="M0 0l7 6 7-6" fill="none" stroke="#111" stroke-width="1.4"/></svg>
    <span>hello@brightdaycare.com</span></div>
  <div class="abs divider" style="left:610px"></div>
  <div class="abs foot-head" style="left:639px;top:3922px">LINKS</div>
  <ul class="abs links">
    <li>Home</li><li>about US</li><li>join us</li><li>help us</li><li>faqs</li><li>contact us</li>
  </ul>
  <div class="abs divider" style="left:759px"></div>
  <div class="abs foot-head" style="left:795px;top:3920px">NEWSLETTER <b>SIGN UP</b></div>
  <p class="abs news-text">Lorem Ipsum Dolor Sit Amet&lt; Consectetuer Adipiscing Elit sed Dam Nonummy Nibh</p>
  <div class="abs news-input">Email</div>
  <div class="abs news-submit">SUBMIT</div>
  <div class="abs copyright">© 2018 Company Name | All Right Reserved</div>
</footer>

</body>
</html>
```